Door Sticker for Loyalty Rewards App

We need to make stickers that will go on the door of the merchants who are part of the Kestro app.

I have attached the Kestro logo, our colours and examples of other door stickers.

Target Market(s)

Millennials

Colors

Designer to choose colors to be used in the design.

Requirements
Must have
• We would like the Kestro logo as the biggest part of the sticker with the text "Effortless Rewards Available Here" and our URL: www.SimplyKestroNow.com (you can drop the www if you want).
• Must use the Kestro colours.

```html
<!DOCTYPE html>
<html lang="en">
<head>
<meta charset="utf-8">
<title>Kestro Door Sticker</title>
<link rel="stylesheet" href="https://fonts.googleapis.com/css2?family=Arimo:wght@700&family=Rokkitt:wght@800&display=swap">
<style>
  :root {
    --pink: #e94b96;
    --navy: #2c2a6a;
    --blue: #2e86c8;
    --indigo: #5a6cb6;
    --violet: #8c50a6;
    --white: #ffffff;
  }
  html, body {
    margin: 0;
    padding: 0;
    width: 1200px;
    height: 489px;
    overflow: hidden;
    background: var(--white);
  }
  .sticker {
    display: block;
    width: 1200px;
    height: 489px;
  }
  .banner-frame { fill: var(--pink); }
  .banner-field { fill: var(--white); }
  .stripe-blue { fill: var(--blue); }
  .stripe-indigo { fill: var(--indigo); }
  .stripe-violet { fill: var(--violet); }
  .badge-ring { fill: var(--white); stroke: var(--pink); stroke-width: 11; }
  .brand-square { fill: var(--pink); }
  .brand-name {
    font-family: "Arimo", Arial, sans-serif;
    font-weight: 700;
    font-size: 92px;
    fill: var(--navy);
  }
  .headline {
    font-family: "Rokkitt", "Rockwell", serif;
    font-weight: 800;
    paint-order: stroke fill;
    stroke: var(--white);
    stroke-width: 8;
    stroke-linejoin: round;
  }
  .headline-top { font-size: 74px; fill: var(--navy); }
  .headline-bottom { font-size: 86px; fill: var(--pink); }
  .underline-bar { fill: var(--blue); stroke: var(--white); stroke-width: 4; }
  .web-address {
    font-family: "Arimo", Arial, sans-serif;
    font-weight: 400;
    font-size: 29px;
    fill: var(--navy);
  }
</style>
</head>
<body>
<svg class="sticker" viewBox="0 0 1200 489" xmlns="http://www.w3.org/2000/svg" role="img" aria-label="Kestro door sticker: Effortless Rewards Available Here">
  <defs>
    <clipPath id="banner-inner">
      <polygon points="432,112 1200,44 1200,458 432,383"/>
    </clipPath>
  </defs>

  <g class="banner">
    <polygon class="banner-frame" points="425,98 1196,29 1196,466 425,393"/>
    <polygon class="banner-field" points="432,112 1178,49 835,421 432,384"/>
    <g clip-path="url(#banner-inner)">
      <polygon class="stripe-blue" points="1178,40 1214,40 870,430 835,430"/>
      <polygon class="stripe-indigo" points="1214,40 1250,40 905,430 870,430"/>
      <polygon class="stripe-violet" points="1250,40 1286,40 940,430 905,430"/>
    </g>
  </g>

  <g class="badge">
    <circle class="badge-ring" cx="231" cy="245" r="224"/>
    <rect class="brand-square" x="181" y="110" width="100" height="100"/>
    <text class="brand-name" x="231" y="320" text-anchor="middle">Kestro</text>
  </g>

  <g class="message">
    <text class="headline headline-top" x="492" y="205" textLength="662" lengthAdjust="spacingAndGlyphs">Effortless Rewards</text>
    <text class="headline headline-bottom" x="495" y="292" textLength="656" lengthAdjust="spacingAndGlyphs">Available Here</text>
    <rect class="underline-bar" x="486" y="303" width="672" height="10" rx="5"/>
    <text class="web-address" x="820" y="352" text-anchor="middle" textLength="420" lengthAdjust="spacingAndGlyphs">www.SimplyKestroNow.com</text>
  </g>
</svg>
</body>
</html>
```